Media Training Presentation (template)

This is a 49-slide power point deck to be used in training clients to deal with the media in various settings. We need a template we can personalize for different clients. The overall color scheme should match our logo. It should look very professional, but also engaging. The word doc contains all of the text, images, and videos for each slide. Also uploaded our logo. Please match/coordinate colors of presentation to the logo colors. If you prefer, you can submit five or six slides showing the overall design and a template for each type of slide, then complete the remainder of the slides within 24 hours if chosen. (Sorry for the quick turnaround…we didn’t know we would need it this quickly!) Thanks for submitting!
Target Market(s)
Government and corporate clients
Look and feel

```html
<!DOCTYPE html>
<html lang="en">
<head>
<meta charset="utf-8">
<title>Media Training Presentation Template</title>
<link href="https://fonts.googleapis.com/css2?family=Montserrat:ital,wght@0,500;0,600;0,700;0,800;1,800&display=swap" rel="stylesheet">
<style>
  :root {
    --page-bg: #58595b;
    --brand-blue: #1458b4;
    --deep-blue: #16469a;
    --bar-grey: #878787;
    --muted-grey: #6f6f6f;
    --white: #ffffff;
    --silver: #d9dde4;
  }
  * { box-sizing: border-box; margin: 0; padding: 0; }
  html, body { width: 1200px; height: 960px; overflow: hidden; }
  body {
    background: var(--page-bg);
    font-family: "Montserrat", Arial, sans-serif;
    position: relative;
  }
  .slide {
    position: absolute;
    width: 347px;
    height: 195px;
    background: var(--white);
    overflow: hidden;
  }
  .col-1 { left: 56px; } .col-2 { left: 422px; } .col-3 { left: 788px; }
  .row-1 { top: 57px; } .row-2 { top: 273px; } .row-3 { top: 489px; } .row-4 { top: 704px; }

  /* header bar */
  .slide-bar {
    position: absolute; top: 15px; left: 0;
    width: 244px; height: 20px; display: flex;
    font-size: 9.5px; font-weight: 600; color: var(--white);
  }
  .bar-section {
    width: 74px; background: var(--brand-blue);
    padding-left: 23px; display: flex; align-items: center; white-space: nowrap;
  }
  .bar-title {
    flex: 1; background: var(--bar-grey);
    padding-left: 4px; display: flex; align-items: center; white-space: nowrap; overflow: hidden;
  }
  .brand {
    position: absolute; top: 16px; left: 252px;
    display: flex; align-items: center; gap: 5px;
  }
  .brand-mark { width: 13px; height: 13px; border: 2px solid var(--brand-blue); flex: none; }
  .brand-name {
    font-size: 9.5px; font-weight: 500; letter-spacing: 1px; color: var(--brand-blue);
  }

  .slide-title {
    position: absolute; left: 24px;
    font-size: 13px; font-weight: 700; color: var(--brand-blue); white-space: nowrap;
  }
  .slide-title .lead { color: var(--muted-grey); }
  .slide-title.two-line { font-size: 11px; line-height: 13px; }

  .page-num {
    position: absolute; left: 320px; top: 170px;
    width: 19px; height: 19px; border-radius: 50%;
    background: var(--brand-blue); color: var(--white);
    font-size: 9px; font-weight: 700;
    display: flex; align-items: center; justify-content: center;
  }

  /* numbered steps */
  .step {
    position: absolute; width: 300px; height: 26px;
    display: grid; grid-template-columns: minmax(0, 1fr) 26px minmax(0, 1fr); column-gap: 13px;
    align-items: center;
    font-size: 7px; font-weight: 600; color: var(--deep-blue);
  }
  .step-left { text-align: right; white-space: nowrap; direction: rtl; }
  .step-right { white-space: nowrap; overflow: visible; }
  .step-num {
    width: 26px; height: 26px; border-radius: 50%;
    background: var(--brand-blue); color: var(--white);
    font-size: 10px; font-weight: 700;
    display: flex; align-items: center; justify-content: center;
  }

  .photo { position: absolute; }
  .bullets {
    position: absolute; left: 222px; top: 80px; list-style: none;
    font-size: 6.5px; font-weight: 600; color: var(--deep-blue);
  }
  .bullets li { height: 14.2px; display: flex; align-items: center; white-space: nowrap; }
  .bullets li::before { content: "•"; width: 12px; font-size: 6px; }

  /* cover */
  .cover-art {
    position: absolute; inset: 0;
    background: linear-gradient(180deg, #3a3f86 0%, #1f66c4 18%, #2a7fd6 55%, #b9c0cc 82%, #1a5bb6 100%);
  }
  .cover-title {
    position: absolute; left: 32px; top: 61px;
    font-style: italic; font-weight: 800; color: var(--silver); line-height: 1;
  }
  .cover-title .small { display: block; font-size: 14px; }
  .cover-title .large { display: block; font-size: 26px; margin-top: 1px; letter-spacing: 0.5px; }
  .cover-meta {
    position: absolute; left: 201px; top: 59px;
    display: grid; grid-template-columns: 68px auto; row-gap: 4px;
    font-size: 10.5px; font-weight: 600; color: var(--white);
  }
  .cover-brand {
    position: absolute; left: 140px; top: 122px;
    display: flex; align-items: center; gap: 4px;
  }
  .cover-brand .brand-mark { width: 11px; height: 11px; border-color: var(--white); }
  .cover-brand .brand-name { font-size: 8px; color: var(--white); }

  .closing { background: var(--brand-blue); display: flex; align-items: center; justify-content: center; }
  .closing h2 { color: var(--white); font-size: 31px; font-weight: 700; }
</style>
</head>
<body>

<!-- 1 cover -->
<section class="slide cover col-1 row-1">
  <div class="cover-art" role="img" aria-label="Illustration of a blue news studio with a curved backdrop and a round silver anchor desk"></div>
  <h1 class="cover-title"><span class="small">MEDIA</span><span class="large">TRAINING</span></h1>
  <dl class="cover-meta">
    <dt>Participant:</dt><dd>Text</dd>
    <dt>Location:</dt><dd>Text</dd>
    <dt>Time:</dt><dd>Text</dd>
  </dl>
  <div class="cover-brand"><span class="brand-mark"></span><span class="brand-name">HARTWELL</span></div>
</section>

<!-- 2 -->
<section class="slide col-2 row-1">
  <div class="slide-bar"><span class="bar-section">Section 1:</span><span class="bar-title">Introduction to Media Training</span></div>
  <div class="brand"><span class="brand-mark"></span><span class="brand-name">HARTWELL</span></div>
  <h2 class="slide-title" style="top:48px"><span class="lead">What is </span>media training?</h2>
  <div class="step" style="left:15px;top:81px"><span class="step-left"></span><span class="step-num">01</span><span class="step-right">It’s not natural</span></div>
  <div class="step" style="left:15px;top:111px"><span class="step-left">It requires practice</span><span class="step-num">02</span><span class="step-right"></span></div>
  <div class="step" style="left:15px;top:141px"><span class="step-left"></span><span class="step-num">03</span><span class="step-right">It’s about developing a mindset</span></div>
  <span class="page-num">2</span>
</section>

<!-- 3 -->
<section class="slide col-3 row-1">
  <div class="slide-bar"><span class="bar-section">Section 1:</span><span class="bar-title">Introduction to Media Training</span></div>
  <div class="brand"><span class="brand-mark"></span><span class="brand-name">HARTWELL</span></div>
  <h2 class="slide-title two-line" style="top:41px">Training and preparation are the difference<br>between success and failure.</h2>
  <div class="photo" role="img" aria-label="Archival interview still of a man speaking on camera" style="left:25px;top:71px;width:309px;height:124px;background:linear-gradient(135deg,#6d7a6c,#a88a78 45%,#4e5a50)"></div>
  <span class="page-num">3</span>
</section>

<!-- 4 -->
<section class="slide col-1 row-2">
  <div class="slide-bar"><span class="bar-section">Section 2:</span><span class="bar-title">Preparation</span></div>
  <div class="brand"><span class="brand-mark"></span><span class="brand-name">HARTWELL</span></div>
  <h2 class="slide-title" style="top:46px">Goals:</h2>
  <div class="step" style="left:24px;top:62px"><span class="step-left"></span><span class="step-num">01</span><span class="step-right">Learn how to prepare</span></div>
  <div class="step" style="left:24px;top:91px"><span class="step-left">Develop a strategy</span><span class="step-num">02</span><span class="step-right"></span></div>
  <div class="step" style="left:24px;top:121px"><span class="step-left"></span><span class="step-num">03</span><span class="step-right">Clarify message</span></div>
  <div class="step" style="left:24px;top:151px"><span class="step-left">Build a practice approach</span><span class="step-num">03</span><span class="step-right"></span></div>
  <span class="page-num">4</span>
</section>

<!-- 5 -->
<section class="slide col-2 row-2">
  <div class="slide-bar"><span class="bar-section">Section 2:</span><span class="bar-title">Preparation</span></div>
  <div class="brand"><span class="brand-mark"></span><span class="brand-name">HARTWELL</span></div>
  <h2 class="slide-title" style="top:42px">What to negotiate?</h2>
  <div class="photo" role="img" aria-label="Photo of a woman and a man shaking hands before an interview, camera in foreground" style="left:23px;top:62px;width:186px;height:123px;background:linear-gradient(120deg,#c9d2dc,#8e9aa8 55%,#2c3440)"></div>
  <ul class="bullets">
    <li>Timing and location</li>
    <li>Rules of recording/broadcast</li>
    <li>Rules of translation</li>
    <li>Questions</li>
    <li>Recording (for accuracy)</li>
  </ul>
  <span class="page-num">5</span>
</section>

<!-- 6 -->
<section class="slide col-3 row-2">
  <div class="slide-bar"><span class="bar-section">Section 2:</span><span class="bar-title">Preparation</span></div>
  <div class="brand"><span class="brand-mark"></span><span class="brand-name">HARTWELL</span></div>
  <h2 class="slide-title" style="top:42px">Create your story</h2>
  <div class="photo" role="img" aria-label="News programme still of officials greeting schoolchildren" style="left:61px;top:63px;width:218px;height:119px;background:linear-gradient(135deg,#b8474a,#d9d3cc 50%,#3c4e6e)"></div>
  <span class="page-num">6</span>
</section>

<!-- 7 -->
<section class="slide col-1 row-3">
  <div class="slide-bar"><span class="bar-section">Section 2:</span><span class="bar-title">Preparation</span></div>
  <div class="brand"><span class="brand-mark"></span><span class="brand-name">HARTWELL</span></div>
  <h2 class="slide-title" style="top:45px">On the record:</h2>
  <div class="step" style="left:14px;top:75px"><span class="step-left"></span><span class="step-num">01</span><span class="step-right">Everything for print</span></div>
  <div class="step" style="left:14px;top:105px"><span class="step-left">Your name for attribution</span><span class="step-num">02</span><span class="step-right"></span></div>
  <div class="step" style="left:14px;top:135px"><span class="step-left"></span><span class="step-num">03</span><span class="step-right">Always assume everything is on the record</span></div>
  <span class="page-num">7</span>
</section>

<!-- 8 -->
<section class="slide col-2 row-3">
  <div class="slide-bar"><span class="bar-section">Section 2:</span><span class="bar-title">Preparation</span></div>
  <div class="brand"><span class="brand-mark"></span><span class="brand-name">HARTWELL</span></div>
  <h2 class="slide-title" style="top:45px">Off the record:</h2>
  <div class="step" style="left:13px;top:75px"><span class="step-left"></span><span class="step-num">01</span><span class="step-right">Not for print</span></div>
  <div class="step" style="left:13px;top:105px"><span class="step-left">Not for attribution</span><span class="step-num">02</span><span class="step-right"></span></div>
  <div class="step" style="left:13px;top:135px"><span class="step-left"></span><span class="step-num">03</span><span class="step-right">Doesn’t mean it won’t be used/printed</span></div>
  <span class="page-num">8</span>
</section>

<!-- 9 -->
<section class="slide col-3 row-3">
  <div class="slide-bar"><span class="bar-section">Section 2:</span><span class="bar-title">Preparation</span></div>
  <div class="brand"><span class="brand-mark"></span><span class="brand-name">HARTWELL</span></div>
  <h2 class="slide-title" style="top:45px">On Background:</h2>
  <div class="step" style="left:27px;top:54px"><span class="step-left"></span><span class="step-num">01</span><span class="step-right">Education</span></div>
  <div class="step" style="left:27px;top:84px"><span class="step-left">Context for print</span><span class="step-num">02</span><span class="step-right"></span></div>
  <div class="step" style="left:27px;top:114px"><span class="step-left"></span><span class="step-num">03</span><span class="step-right">Can be used with attribution</span></div>
  <div class="step" style="left:27px;top:144px"><span class="step-left">Attribution to be negotiated</span><span class="step-num">03</span><span class="step-right"></span></div>
  <span class="page-num">9</span>
</section>

<!-- 10 -->
<section class="slide col-1 row-4">
  <div class="slide-bar"><span class="bar-section">Section 2:</span><span class="bar-title">Preparation</span></div>
  <div class="brand"><span class="brand-mark"></span><span class="brand-name">HARTWELL</span></div>
  <h2 class="slide-title" style="top:43px">Preparation Matters!</h2>
  <div class="photo" role="img" aria-label="Video still of a televised sit-down interview on a dark studio set" style="left:61px;top:64px;width:220px;height:123px;background:linear-gradient(180deg,#111 0%,#5a1a1a 40%,#2a0c0c 100%)"></div>
  <span class="page-num">10</span>
</section>

<!-- 11 -->
<section class="slide col-2 row-4">
  <div class="slide-bar"><span class="bar-section">Section 2:</span><span class="bar-title">Preparation</span></div>
  <div class="brand"><span class="brand-mark"></span><span class="brand-name">HARTWELL</span></div>
  <h2 class="slide-title" style="top:43px">Schedule</h2>
  <div class="step" style="left:27px;top:55px"><span class="step-left"></span><span class="step-num">01</span><span class="step-right">Develop Q/A</span></div>
  <div class="step" style="left:27px;top:85px"><span class="step-left">Write answers but also vocalize</span><span class="step-num">02</span><span class="step-right"></span></div>
  <div class="step" style="left:27px;top:115px"><span class="step-left"></span><span class="step-num">03</span><span class="step-right">Practice: table</span></div>
  <div class="step" style="left:27px;top:145px"><span class="step-left">Practice: mock</span><span class="step-num">03</span><span class="step-right"></span></div>
  <span class="page-num">11</span>
</section>

<!-- 12 -->
<section class="slide closing col-3 row-4">
  <h2>Thank You</h2>
</section>

</body>
</html>
```